VORKEL COMPOSITES INC website in USA

VORKEL COMPOSITES INC incorporated and operated in USA needs a completely new design of website. This Wyoming based company is a importer and distributor of composites material to supply mainly to American and Canadian/Mexican customers. Our main products includes Carbon Fiber, Aramid Fiber, Glass Fiber, Basalt Fiber, High Silica Glass, Quartz Fiber, S-Glass, Alumina Fiber, Vacuum Auxiliary.

We are one stop composites solution provider for Automotive, Aerospace, Construction, Electrical and Machinery industries.

We are exclusive sales company in North America for DORAQ composites produced from China and their other Asia facilities.

Target Market(s)

USA and Canada

Industry/Entity Type

Composites materials

Coding

Coded - Design and coding required

Number of Pages Required

5+ page

Requirements
Nice to have
• Color theme to match our corporate logo VORKEL. VORKEL stands for Vantor Omniline Reliant Kinetic Export Lodge

```html
<!DOCTYPE html>
<html lang="en">
<head>
<meta charset="utf-8">
<title>Contact Us – VORKEL COMPOSITES INC</title>
<link href="https://fonts.googleapis.com/css2?family=Montserrat:wght@500;600;700&family=Open+Sans:wght@400;600;700&display=swap" rel="stylesheet">
<style>
:root{
  --navy:#13254a;
  --navy-deep:#0f1d3a;
  --navy-mid:#1b3260;
  --gold:#b58a3a;
  --ink:#1b2433;
  --muted:#5f6673;
  --line:#d9dde5;
  --soft:#f4f6fa;
  --white:#ffffff;
}
*{box-sizing:border-box;margin:0;padding:0}
html,body{width:1200px;height:4028px;overflow:hidden}
body{font-family:"Open Sans",Arial,sans-serif;color:var(--ink);background:var(--white)}
h1,h2,h3,h4{font-family:"Montserrat",Arial,sans-serif}
.container{width:1061px;margin:0 auto}

/* Header */
.site-header{height:96px;display:flex;align-items:center;justify-content:space-between;padding:0 60px 0 92px;border-bottom:1px solid var(--line)}
.brand{display:flex;align-items:center;gap:10px;font-family:"Open Sans",sans-serif;font-weight:700;font-size:26px;color:var(--navy)}
.brand-mark{width:22px;height:22px;background:var(--gold)}
.main-nav{display:flex;align-items:center;gap:34px;font-size:16px;color:var(--ink)}
.main-nav .active{color:var(--gold)}
.partner-btn{border:1.5px solid var(--ink);border-radius:16px;padding:5px 14px;font-size:12px;font-weight:600;margin-left:18px}

/* Hero */
.hero{height:345px;background:linear-gradient(120deg,#2c3d5e 0%,#1a2c50 45%,#132347 100%);display:flex;flex-direction:column;align-items:center;justify-content:center;color:var(--white);text-align:center}
.hero h1{font-size:46px;font-weight:700;margin-bottom:20px}
.hero p{font-size:18px;opacity:.9}

/* Contact */
.contact{height:1163px;padding-top:84px}
.contact-grid{display:grid;grid-template-columns:495px 495px;gap:71px}
.info-card{background:var(--soft);border-radius:8px;padding:52px 52px 52px;height:667px}
.info-card h2,.form-card h2{font-size:34px;font-weight:700;color:var(--navy);margin-bottom:34px}
.info-item{display:flex;gap:16px;margin-bottom:30px}
.info-item svg{flex:none;margin-top:4px}
.info-item h4{font-size:16px;font-weight:600;color:var(--ink);margin-bottom:8px}
.info-item p{font-size:16px;color:var(--muted)}
.info-item small{display:block;font-size:11px;color:var(--muted);margin-top:8px}
.hours-box{background:var(--white);border-radius:6px;padding:24px 26px;margin-top:14px}
.hours-box h4{font-size:16px;font-weight:600;margin-bottom:20px}
.hours-row{display:flex;justify-content:space-between;font-size:16px;color:var(--muted);margin-bottom:16px}
.form-card{background:var(--white);border-radius:8px;box-shadow:0 4px 22px rgba(19,37,74,.1);padding:52px 52px;height:992px}
.form-row{display:grid;grid-template-columns:1fr 1fr;gap:18px}
.field{margin-bottom:28px}
.field label{display:block;font-size:16px;font-weight:600;margin-bottom:12px}
.field label b{color:#d33;font-weight:600}
.input{height:52px;border:1.5px solid var(--line);border-radius:5px;background:var(--white)}
.select{height:56px;border:1.5px solid var(--line);border-radius:5px;background:#eef0f4;display:flex;align-items:center;justify-content:space-between;padding:0 16px 0 22px;font-size:16px}
.textarea{height:130px;border:1.5px solid var(--line);border-radius:5px;padding:14px 16px;font-size:15px;color:#7b808a;line-height:1.6}
.btn-gold{background:var(--gold);color:var(--white);border-radius:5px;text-align:center;font-weight:600;font-size:16px;height:46px;line-height:46px}

/* Help */
.help{height:770px;background:var(--soft);padding-top:82px;text-align:center}
.help h2{font-size:40px;font-weight:700;color:var(--navy);margin-bottom:22px}
.help .lead{font-size:18px;color:var(--muted);margin-bottom:52px}
.help-grid{display:grid;grid-template-columns:repeat(3,332px);gap:32px;justify-content:space-between}
.help-card{background:var(--white);border-radius:6px;height:452px;padding:58px 34px 0;box-shadow:0 2px 10px rgba(19,37,74,.05)}
.help-card h3{font-size:25px;font-weight:700;color:var(--navy);margin:34px 0 22px}
.help-card p{font-size:16px;line-height:1.75;color:var(--muted);height:118px}
.btn-outline{display:inline-block;border:2px solid var(--navy);border-radius:5px;padding:15px 34px;font-size:16px;font-weight:600;color:var(--navy);margin-top:30px}

/* Location */
.location{height:427px;background:var(--navy-deep);color:var(--white);text-align:center;padding-top:130px}
.location h3{font-size:20px;font-weight:700;margin:14px 0 10px}
.location p{font-size:16px}
.location small{display:block;font-size:12px;margin-top:8px;opacity:.85}

/* CTA */
.cta{height:460px;background:linear-gradient(180deg,var(--navy-deep),var(--navy-mid));color:var(--white);text-align:center;padding-top:100px}
.cta h2{font-size:46px;font-weight:700;margin-bottom:28px}
.cta p{font-size:19px;line-height:1.75;width:780px;margin:0 auto 42px}
.cta-actions{display:flex;justify-content:center;gap:18px}
.cta-actions span{display:flex;align-items:center;gap:8px;height:56px;padding:0 34px;border-radius:5px;font-size:16px;font-weight:600}
.cta-call{background:var(--gold)}
.cta-msg{border:2px solid var(--white)}

/* Footer */
.site-footer{height:767px;background:#0e1a33;color:#e6e9ef;padding-top:60px}
.footer-grid{display:grid;grid-template-columns:372px 372px 317px}
.site-footer h4{font-size:19px;font-weight:700;color:var(--white);margin-bottom:12px}
.site-footer h4::after{content:"";display:block;width:40px;height:3px;background:var(--gold);margin-top:10px}
.footer-col p{font-size:15px;line-height:1.9;width:320px;margin-top:22px}
.footer-col ul{list-style:none;margin-top:22px}
.footer-col li{font-size:15px;margin-bottom:16px;display:flex;align-items:center;gap:8px}
.footer-col li i{color:var(--gold);font-style:normal}
.socials{display:flex;gap:14px;margin-top:24px}
.socials span{width:36px;height:36px;border-radius:50%;background:#233353}
.newsletter{margin-top:70px;width:320px}
.newsletter p{margin-top:22px;font-size:15px;line-height:1.9}
.news-input{height:42px;background:var(--white);border-radius:3px;margin-top:8px;padding:0 14px;line-height:42px;font-size:12px;color:#8a8f99}
.news-btn{height:40px;background:var(--gold);border-radius:3px;margin-top:16px;text-align:center;line-height:40px;font-size:12px;font-weight:700;color:var(--navy-deep)}
.copyright{text-align:center;font-size:13px;color:#c7ccd6;margin-top:74px}
</style>
</head>
<body>

<header class="site-header">
  <div class="brand"><span class="brand-mark"></span>DORAQ</div>
  <nav class="main-nav">
    <span>Home</span><span>Products</span><span>Industries</span><span>About</span><span class="active">Contact</span>
    <span class="partner-btn">DORAQ Partner</span>
  </nav>
</header>

<section class="hero" role="img" aria-label="Dark navy photo of a person working at a laptop behind the page title">
  <h1>Contact Us</h1>
  <p>Get in touch with our team of composite materials experts</p>
</section>

<section class="contact">
  <div class="container contact-grid">
    <aside class="info-card">
      <h2>Get In Touch</h2>
      <div class="info-item">
        <svg width="16" height="20" viewBox="0 0 16 20"><path d="M8 0a7 7 0 0 0-7 7c0 5 7 13 7 13s7-8 7-13a7 7 0 0 0-7-7zm0 10a3 3 0 1 1 0-6 3 3 0 0 1 0 6z" fill="#b58a3a"/></svg>
        <div><h4>Headquarters</h4><p>Wyoming, United States</p><small>Serving North America</small></div>
      </div>
      <div class="info-item">
        <svg width="18" height="18" viewBox="0 0 24 24"><path d="M6.6 10.8a15 15 0 0 0 6.6 6.6l2.2-2.2a1 1 0 0 1 1-.25 11.4 11.4 0 0 0 3.6.57 1 1 0 0 1 1 1V20a1 1 0 0 1-1 1A17 17 0 0 1 3 4a1 1 0 0 1 1-1h3.5a1 1 0 0 1 1 1c0 1.25.2 2.45.57 3.57a1 1 0 0 1-.25 1z" fill="#b58a3a"/></svg>
        <div><h4>Phone</h4><p>+1 (307) 555-0148</p></div>
      </div>
      <div class="info-item">
        <svg width="18" height="18" viewBox="0 0 20 20"><circle cx="10" cy="10" r="9" fill="#b58a3a"/><path d="M10 5v5l3 2" stroke="#fff" stroke-width="2" fill="none"/></svg>
        <div><h4>Business Hours</h4><p>Monday - Friday: 8:00 AM - 5:00 PM MST</p></div>
      </div>
      <div class="hours-box">
        <h4>Office Hours</h4>
        <div class="hours-row"><span>Monday - Friday:</span><span>8:00 AM - 5:00 PM</span></div>
        <div class="hours-row"><span>Saturday:</span><span>Closed</span></div>
        <div class="hours-row"><span>Sunday:</span><span>Closed</span></div>
      </div>
    </aside>

    <div class="form-card">
      <h2>Send Us a Message</h2>
      <div class="form-row">
        <div class="field"><label>First Name <b>*</b></label><div class="input"></div></div>
        <div class="field"><label>Last Name <b>*</b></label><div class="input"></div></div>
      </div>
      <div class="form-row">
        <div class="field"><label>Email Address <b>*</b></label><div class="input"></div></div>
        <div class="field"><label>Phone Number</label><div class="input"></div></div>
      </div>
      <div class="field"><label>Company Name</label><div class="input"></div></div>
      <div class="field"><label>Industry <b>*</b></label><div class="select">Select Industry<span>⌄</span></div></div>
      <div class="field"><label>Product Interest</label><div class="select">Select Product<span>⌄</span></div></div>
      <div class="field"><label>Message <b>*</b></label><div class="textarea">Please describe your application, requirements, or any specific technical needs...</div></div>
      <div class="btn-gold">Send Message</div>
    </div>
  </div>
</section>

<section class="help">
  <div class="container">
    <h2>How Can We Help You?</h2>
    <p class="lead">Choose the contact method that works best for your needs</p>
    <div class="help-grid">
      <article class="help-card">
        <svg width="56" height="44" viewBox="0 0 56 44"><ellipse cx="22" cy="16" rx="20" ry="14" fill="#b58a3a"/><path d="M8 26l-4 10 12-6z" fill="#b58a3a"/><ellipse cx="38" cy="26" rx="16" ry="11" fill="#b58a3a"/><path d="M48 34l4 8-10-5z" fill="#b58a3a"/></svg>
        <h3>General Inquiries</h3>
        <p>Have questions about our products or services? Our team is ready to provide you with the information you need.</p>
        <span class="btn-outline">Contact Us</span>
      </article>
      <article class="help-card">
        <svg width="44" height="44" viewBox="0 0 44 44"><rect x="14" y="2" width="8" height="22" rx="2" fill="#b58a3a"/><circle cx="28" cy="28" r="9" fill="none" stroke="#b58a3a" stroke-width="5"/><rect x="6" y="38" width="32" height="5" fill="#b58a3a"/></svg>
        <h3>Technical Support</h3>
        <p>Need technical specifications, material selection guidance, or application support? Our experts are here to help.</p>
        <span class="btn-outline">Get Support</span>
      </article>
      <article class="help-card">
        <svg width="50" height="44" viewBox="0 0 50 44"><path d="M2 4h8l6 24h26l6-18H13" fill="#b58a3a"/><circle cx="19" cy="38" r="4" fill="#b58a3a"/><circle cx="38" cy="38" r="4" fill="#b58a3a"/></svg>
        <h3>Sales &amp; Quotes</h3>
        <p>Ready to place an order or request a quote? Contact our sales team for pricing and availability.</p>
        <span class="btn-outline">Request a Quote</span>
      </article>
    </div>
  </div>
</section>

<section class="location">
  <svg width="64" height="58" viewBox="0 0 64 58"><path d="M2 20l16-6v44L2 58zM22 14l20 8v36l-20-8zM46 22l16-6v36l-16 6z" fill="#b58a3a"/><circle cx="32" cy="14" r="12" fill="#b58a3a"/><circle cx="32" cy="13" r="5" fill="#0f1d3a"/></svg>
  <h3>Wyoming, USA</h3>
  <p>Strategic location serving North American markets</p>
  <small>Contact us for specific location details</small>
</section>

<section class="cta">
  <h2>Ready to Get Started?</h2>
  <p>Contact us today to discuss your composite material needs and discover how our solutions can enhance your applications.</p>
  <div class="cta-actions">
    <span class="cta-call"><svg width="14" height="14" viewBox="0 0 24 24"><path d="M6.6 10.8a15 15 0 0 0 6.6 6.6l2.2-2.2a1 1 0 0 1 1-.25 11.4 11.4 0 0 0 3.6.57 1 1 0 0 1 1 1V20a1 1 0 0 1-1 1A17 17 0 0 1 3 4a1 1 0 0 1 1-1h3.5a1 1 0 0 1 1 1c0 1.25.2 2.45.57 3.57a1 1 0 0 1-.25 1z" fill="#fff"/></svg>Call Now</span>
    <span class="cta-msg"><svg width="16" height="12" viewBox="0 0 16 12"><rect width="16" height="12" rx="1" fill="#fff"/><path d="M1 1l7 6 7-6" stroke="#1b3260" stroke-width="1.5" fill="none"/></svg>Send a Message</span>
  </div>
</section>

<footer class="site-footer">
  <div class="container">
    <div class="footer-grid">
      <div class="footer-col">
        <h4>VORKEL COMPOSITES</h4>
        <p>Your trusted partner for advanced composite materials in North America. Exclusive distributor of DORAQ high-performance fibers.</p>
        <div class="socials"><span></span><span></span><span></span><span></span></div>
        <div class="newsletter">
          <h4>Newsletter</h4>
          <p>Subscribe to get updates on new products, industry insights, and technical resources.</p>
          <div class="news-input">Your Email Address</div>
          <div class="news-btn">Subscribe</div>
        </div>
      </div>
      <div class="footer-col">
        <h4>Quick Links</h4>
        <ul>
          <li><i>›</i>Home</li><li><i>›</i>Products</li><li><i>›</i>Industries</li><li><i>›</i>About Us</li><li><i>›</i>Contact</li>
        </ul>
      </div>
      <div class="footer-col">
        <h4>Contact Info</h4>
        <ul>
          <li><i>●</i>Wyoming, USA</li>
          <li><i>●</i>+1 (307) 555-0148</li>
          <li><i>●</i>Contact Form</li>
          <li><i>●</i>Mon-Fri: 8:00 AM - 5:00 PM</li>
        </ul>
      </div>
    </div>
    <p class="copyright">© 2025 VORKEL COMPOSITES INC. All Rights Reserved. | Exclusive North American Distributor for DORAQ Composites</p>
  </div>
</footer>

</body>
</html>
```